Modern Attractive Letterhead for Veterinary House Call Business.

A letterhead which can be printed on A4, A5 and A6 paper sizes.
To have: ( our files to be uploaded)
1. Logo with Text
2. telephone
3. email
4. website
5. Address

Target Market(s)

60-85year mainly women pet owners. Also market include families, young professionals, busy people who have dogs and cats

Industry/Entity Type

Business

Requirements
Must have
• 1. Logo with Text ( provided)
• 2. telephone
• 3. email
• 4. website
• 5. Address
Nice to have
• Needs to be modern, preferably warm and caring in nature( if possible )
Should not have
• difficulty in printing A5 and A6

```html
<!DOCTYPE html>
<html lang="en">
<head>
<meta charset="utf-8">
<title>Kind Paw Vets Letterhead</title>
<link rel="stylesheet" href="https://fonts.googleapis.com/css2?family=Arimo:wght@400;700&display=swap">
<style>
  :root {
    --backdrop: #ece8e2;
    --paper: #ffffff;
    --brand-blue: #3a6d9e;
    --brand-blue-dark: #2d5782;
    --band-grey: #cfd0d2;
    --band-grey-dark: #a9abae;
    --ink: #222222;
    --contact-ink: #ffffff;
  }
  * { box-sizing: border-box; margin: 0; padding: 0; }
  html, body { width: 1200px; height: 1000px; overflow: hidden; }
  body {
    background: var(--backdrop);
    font-family: "Arimo", Arial, sans-serif;
    color: var(--ink);
    position: relative;
  }
  .letterhead {
    position: absolute;
    left: 270px;
    top: 33px;
    width: 660px;
    height: 934px;
    background: var(--paper);
    box-shadow: 0 4px 18px rgba(0,0,0,0.18);
    overflow: hidden;
  }
  .letterhead-bands { position: absolute; inset: 0; }
  .brand-name {
    position: absolute;
    left: 30px;
    top: 38px;
    display: flex;
    align-items: center;
    gap: 10px;
    font-size: 24px;
    font-weight: 700;
    color: var(--brand-blue);
    letter-spacing: 0.5px;
  }
  .brand-mark {
    width: 14px; height: 14px;
    border-radius: 50%;
    background: var(--brand-blue);
  }
  .contact-list {
    position: absolute;
    right: 40px;
    top: 22px;
    list-style: none;
    color: var(--contact-ink);
    font-size: 12.5px;
    font-weight: 700;
  }
  .contact-list li {
    display: flex;
    align-items: center;
    gap: 7px;
    line-height: 21px;
  }
  .contact-list svg { width: 12px; height: 12px; flex: none; }
  .letter-body {
    position: absolute;
    left: 52px;
    right: 30px;
    top: 160px;
    font-size: 17.5px;
    line-height: 21px;
  }
  .letter-body p {
    text-align: left;
    text-indent: 150px;
    margin-bottom: 21px;
  }
  .sign-off {
    position: absolute;
    left: 52px;
    top: 616px;
    font-size: 17.5px;
  }
  .signature {
    width: 90px;
    height: 34px;
    margin: 8px 0 6px 10px;
    background: linear-gradient(90deg, rgba(58,109,158,0.15), rgba(58,109,158,0.35));
    border-radius: 4px;
  }
  .website {
    position: absolute;
    left: 0; right: 0;
    bottom: 22px;
    text-align: center;
    padding-left: 120px;
    font-size: 12.5px;
    font-weight: 700;
    color: var(--brand-blue);
  }
</style>
</head>
<body>
  <article class="letterhead">
    <svg class="letterhead-bands" width="660" height="934" viewBox="0 0 660 934" aria-hidden="true">
      <polygon points="0,0 320,0 300,40 240,130 0,130" fill="var(--band-grey)"/>
      <polygon points="290,0 660,0 660,112 260,112 300,40" fill="var(--brand-blue)"/>
      <polygon points="260,112 300,40 290,112" fill="var(--brand-blue-dark)"/>
      <polygon points="470,934 660,934 660,810 600,810" fill="var(--band-grey-dark)"/>
      <polygon points="0,884 120,884 150,934 0,934" fill="var(--brand-blue)"/>
      <polygon points="110,934 160,880 660,880 660,934" fill="var(--band-grey)"/>
      <polygon points="120,884 160,880 150,934" fill="var(--brand-blue-dark)"/>
    </svg>

    <div class="brand-name"><span class="brand-mark"></span>Kind Paw Vets</div>

    <ul class="contact-list">
      <li>
        <svg viewBox="0 0 12 12"><circle cx="6" cy="6" r="5.3" fill="none" stroke="#fff" stroke-width="1.2"/><path d="M4 3.3l1 1.3-.6.8a4 4 0 0 0 2.2 2.2l.8-.6 1.3 1-.7 1C5.8 9 3 6.2 3 4z" fill="#fff"/></svg>
        0491570156
      </li>
      <li>
        <svg viewBox="0 0 12 12"><circle cx="6" cy="6" r="5.3" fill="none" stroke="#fff" stroke-width="1.2"/><rect x="3" y="4" width="6" height="4" fill="none" stroke="#fff" stroke-width="1"/><path d="M3 4l3 2.3L9 4" fill="none" stroke="#fff" stroke-width="1"/></svg>
        hello@kindpawvets.com.au
      </li>
      <li>
        <svg viewBox="0 0 12 12"><circle cx="6" cy="6" r="5.3" fill="none" stroke="#fff" stroke-width="1.2"/><circle cx="6" cy="6" r="2.3" fill="#fff"/></svg>
        PO Box 482 Elmvale QLD 4100
      </li>
    </ul>

    <div class="letter-body">
      <p>Lorem Ipsum is simply dummy text of the printing and typesetting industry. Lorem Ipsum has been the industry's standard dummy text ever since the 1500s, when an unknown printer took a galley of type and scrambled it to make a type specimen book. It has survived not only five centuries, but also the leap into electronic typesetting, remaining essentially unchanged. It was popularised in the 1960s with the release of Typemark sheets containing Lorem Ipsum passages, and more recently with desktop publishing software like Quillon PageDesk including versions of Lorem Ipsum.</p>
      <p>It is a long established fact that a reader will be distracted by the readable content of a page when looking at its layout. The point of using Lorem Ipsum is that it has a more-or-less normal distribution of letters, as opposed to using 'Content here, content here', making it look like readable English. Many desktop publishing packages and web page editors now use Lorem Ipsum as their default model text, and a search for 'lorem ipsum' will uncover many web sites still in their infancy. Various versions have evolved over the years, sometimes by accident, sometimes on purpose (injected humour and the like).</p>
    </div>

    <div class="sign-off">
      <div>Yours Manager</div>
      <div class="signature" role="img" aria-label="Handwritten signature"></div>
      <div>Sam Carter</div>
    </div>

    <div class="website">www.kindpawvets.com.au</div>
  </article>
</body>
</html>
```